Gaming company needs web presence

PLEASE NOTE: We need just a simple web site. We are at least a year away from launching our first product, so the site only needs a small amount of information on it. The only people who will be visiting the web site are prospective employees, prospective investors who want a little information on the company, journalists who want a little more information, and people in the games industry who will visit to read blog posts about the development of our first game.

Brindle Hollow Studios is a new gaming company that wants to change how people think about video games. We are making games that we think can be so interesting to watch that people might want to tune into them instead of the TV.

The games we make are sophisticated, they are not for children, and we want to project an image of being serious about our craft and the brand we're trying to create. Our games are heavily focused on players interacting with each other in sophisticated ways: to negotiate, to compete, to fight, to come to each other's rescue, to cheer each other on, or to simply watch each other in awe.

We do not want a site that features lots of video game cliches like joysticks, 8 bit graphics, science fiction themes, or military themes. We are focused on craftsmanship, so we'd like to project a sense of precision, pride and deep purpose.

The purpose of this website is to create an image of our company that can help us recruit like-minded craftspeople and help find business partners. There will be no e-commerce, account creation, or forums for some time. The site should have:
-A front page that describes our business
-A section that describes our first game (we have only one for now)
-A section for employees to write blog posts. There should be something on the home page that shows links to the latest 3 blog posts.
-A section about founders that shows information about them.
-Contact information, lets people send us email

Our first game is one that looks very realistic. It takes place on a tropical island. We can't say a lot more about it in public yet, but I will say these things: it is not a game that children will play, it is not very violent, it would look more like a film than a typical video game.

And the site should be easily extendable when we have more content and more categories of content.

I've attached our official company logo with a color scheme we've been using, plus an alternate version of the logo. Please use this as a starting point for the web site's visual design. Also, I do not think it is necessary to use the dark background in the logo as the background throughout the site. I wouldn't rule it out, but I'd like to see some proposals with lighter backgrounds.

We need to be able to get code from you so that we can drop it on our server and get it running without extra effort. We need to be able to add content for Blog posts easily as well, so please indicate how that would work.
Updates

Hello everyone, Thanks for all of the great submissions so far. There are some important things I'd like to relay to everyone: We are at least a year away from launching our first game, so we only need a simple web site. Unfortunately, we can't share any screenshots or details about our first game yet. All of these submissions look great, but are far too complicated. Also, I really want to stress that we don't want to feature stock photography of people playing games, especially of children playing games. In fact, since we don't want to release any screenshots of our games and we don't have any good photography of ourselves working, it's best if there are no photographic images on the site for now.

Hello designers, Can you let me know if your designs include all the code that would let us drop the files on to our web server and easily get it up and running? Also, can you tell me how the blog posts would be created? Does your code run on a CMS? Thanks, Pellman

Hi Designers, we will be hosting this site with Wordpress, so we would prefer to have submissions ready to go on a Wordpress server. Thanks!

Target Market(s)

Investors, prospective employees, press, blog post readers.

Industry/Entity Type

Business

Font styles to use
Sans Serif

Requirements
Must have
• Simplicity first. Please use a color palette and fonts that match our logo.
Should not have
• Video game cliches. Flash animations or menus.
No children.
No photographs of people playing games.

(I realize this is very limiting, but we're keeping the sits as simple as possible for now)

```html
<!DOCTYPE html>
<html lang="en">
<head>
<meta charset="utf-8">
<title>Brindle Hollow Studios — Blog</title>
<link rel="stylesheet" href="https://fonts.googleapis.com/css2?family=Ubuntu:wght@300;400;500;700&family=Alfa+Slab+One&display=swap">
<style>
  :root {
    --wood-dark: #3f1d0a;
    --wood: #552a10;
    --wood-light: #66351a;
    --cream: #faf8e6;
    --white: #ffffff;
    --orange: #c9692c;
    --orange-soft: #e3a46a;
    --slogan-brown: #5a4030;
    --ink: #2b1a10;
    --grey: #a2a2a2;
    --grey-dark: #6e6e6e;
    --footer: #4a2108;
  }
  * { box-sizing: border-box; margin: 0; padding: 0; }
  html, body { width: 709px; height: 1200px; overflow: hidden; }
  body { position: relative; background: var(--white); font-family: "Ubuntu", sans-serif; color: var(--ink); }
  .abs { position: absolute; }

  /* Header */
  .site-header {
    position: absolute; left: 0; top: 0; width: 709px; height: 323px;
    background: linear-gradient(180deg, var(--wood-dark) 0%, var(--wood) 45%, var(--wood-light) 100%);
  }
  .main-nav { position: absolute; left: 94px; top: 37px; display: flex; gap: 0; }
  .main-nav a {
    color: var(--white); text-decoration: none; font-size: 8.5px; letter-spacing: .2px;
    margin-right: 26px; padding-bottom: 3px;
  }
  .main-nav a.is-active { border-bottom: 1px solid var(--orange-soft); }
  .header-social { position: absolute; left: 565px; top: 36px; display: flex; gap: 1px; }
  .header-social span {
    width: 12px; height: 12px; border-radius: 50%; background: #d9d2c8; display: block;
  }
  .brand-mark {
    position: absolute; left: 0; top: 112px; width: 709px; text-align: center;
    color: var(--white); font-weight: 700; line-height: 1; text-transform: uppercase;
  }
  .brand-mark .line-1 { display: block; font-size: 60px; letter-spacing: 3px; }
  .brand-mark .line-2 { display: block; font-size: 40px; letter-spacing: 10px; margin-top: 24px; }
  .pointer { position: absolute; left: 320px; top: 322px; }

  /* Slogan band */
  .slogan-band { position: absolute; left: 0; top: 323px; width: 709px; height: 122px; background: var(--cream); }
  .slogan { position: absolute; left: 0; top: 28px; width: 709px; text-align: center; font-family: "Alfa Slab One", serif; font-size: 22px; letter-spacing: 2px; line-height: 27px; }
  .slogan .line-dark { display: block; color: var(--slogan-brown); }
  .slogan .line-light { display: block; color: var(--orange-soft); }

  /* Post */
  .post-title { left: 94px; top: 460px; font-size: 17px; font-weight: 400; color: var(--ink); letter-spacing: .2px; }
  .post-meta { top: 466px; font-size: 6.5px; color: var(--grey); display: flex; align-items: center; gap: 4px; }
  .post-byline { left: 96px; top: 483px; font-size: 8px; color: var(--grey-dark); font-weight: 500; }
  .post-byline a { color: var(--orange); text-decoration: none; }
  .media {
    border: 2px solid var(--orange); 
  }
  .media-hero { left: 94px; top: 502px; width: 388px; height: 179px; background: linear-gradient(160deg, #2d3a36 0%, #1f2a25 45%, #3e4a3a 70%, #1a2320 100%); }
  .media-fire { left: 337px; top: 726px; width: 152px; height: 84px; background: linear-gradient(120deg, #2c2a26 0%, #6b5a44 45%, #3a342c 100%); }
  .media-tower { left: 99px; top: 835px; width: 126px; height: 106px; background: linear-gradient(180deg, #b8aa92 0%, #8a7a64 55%, #3e3428 100%); }

  .older-posts { left: 95px; top: 702px; font-size: 8px; font-weight: 700; color: var(--orange); display: flex; align-items: center; gap: 5px; }
  .excerpt { font-size: 7px; line-height: 9px; color: var(--grey); font-weight: 300; }
  .excerpt p + p { margin-top: 9px; }
  .excerpt-a { left: 97px; top: 726px; width: 232px; }
  .excerpt-b { left: 239px; top: 835px; width: 250px; }

  /* Sidebar */
  .widget-title { font-size: 11px; font-weight: 400; color: var(--ink); }
  .widget-list { list-style: none; }
  .widget-list li { position: relative; padding-left: 14px; font-size: 8px; color: var(--grey); height: 15px; line-height: 10px; font-weight: 300; }
  .widget-list li::before { content: ""; position: absolute; left: 0; top: 2px; width: 5px; height: 5px; border-radius: 50%; background: var(--orange); }

  /* Comments */
  .comments-band { position: absolute; left: 0; top: 968px; width: 709px; height: 170px; background: var(--cream); }
  .comments-title { position: absolute; left: 97px; top: 14px; font-size: 17px; font-weight: 400; color: var(--ink); }
  .comment { position: absolute; top: 54px; width: 272px; }
  .avatar { position: absolute; left: 0; top: 0; width: 54px; height: 54px; border: 1px solid #e4e2d2; background: var(--cream); }
  .comment-body { position: absolute; left: 63px; top: 0; width: 205px; }
  .comment-author { font-size: 7.5px; font-weight: 700; color: var(--ink); line-height: 10px; }
  .comment-sub { font-size: 7.5px; color: var(--ink); line-height: 10px; }
  .comment-text { font-size: 7px; line-height: 9px; color: var(--grey); margin-top: 8px; font-weight: 300; }
  .comment-reply { display: inline-block; margin-top: 9px; font-size: 7.5px; color: var(--ink); text-decoration: underline; }

  /* Footer */
  .site-footer { position: absolute; left: 0; top: 1138px; width: 709px; height: 62px; background: var(--footer); }
  .footer-brand { position: absolute; left: 101px; top: 12px; color: var(--white); font-weight: 700; text-transform: uppercase; line-height: 1; }
  .footer-brand .line-1 { display: block; font-size: 14px; letter-spacing: 1px; }
  .footer-brand .line-2 { display: block; font-size: 9px; letter-spacing: 3.5px; margin-top: 5px; }
  .footer-legal { position: absolute; left: 388px; top: 20px; font-size: 6.5px; color: var(--white); }
  .footer-social { position: absolute; left: 541px; top: 19px; display: flex; gap: 9px; }
  .footer-social span { width: 10px; height: 10px; border-radius: 50%; background: var(--white); display: block; }
</style>
</head>
<body>

<header class="site-header">
  <nav class="main-nav">
    <a href="#">HOME</a>
    <a href="#">ABOUT US</a>
    <a href="#">SERVICES</a>
    <a href="#" class="is-active">BLOG</a>
    <a href="#">REVIEWS</a>
    <a href="#">CONTACT US</a>
  </nav>
  <div class="header-social" aria-label="Social links">
    <span></span><span></span><span></span><span></span>
  </div>
  <div class="brand-mark">
    <span class="line-1">Brindle Hollow</span>
    <span class="line-2">Studios</span>
  </div>
</header>

<section class="slogan-band">
  <h2 class="slogan">
    <span class="line-dark">THE WORLD WANTS TO SEE</span>
    <span class="line-light">YOUR SKILL AND CREATIVITY</span>
  </h2>
</section>

<svg class="pointer" width="50" height="25" viewBox="0 0 50 25" aria-hidden="true">
  <polygon points="0,0 50,0 25,25" fill="#66351a"/>
</svg>

<main>
  <h1 class="abs post-title">LACUS LEO FERMENT</h1>
  <div class="abs post-meta" style="left:363px;">
    <svg width="7" height="7" viewBox="0 0 10 10"><circle cx="5" cy="5" r="4" fill="none" stroke="#c9692c" stroke-width="1.6"/><path d="M5 2.6V5h2" stroke="#c9692c" stroke-width="1.2" fill="none"/></svg>
    05 Hours ago
  </div>
  <div class="abs post-meta" style="left:430px;">
    <svg width="8" height="7" viewBox="0 0 12 10"><path d="M1 1h7v5H4l-2 2V6H1z" fill="#6b4a36"/><path d="M9 3h2v5h-1v2l-2-2H5V7h4z" fill="#6b4a36"/></svg>
    20 comments
  </div>
  <p class="abs post-byline">written by Mara Vellin, In <a href="#">interviews with brindle hollow studios</a></p>

  <div class="abs media media-hero" role="img" aria-label="Illustration of a hooded figure crouched before an overgrown jungle temple"></div>

  <div class="abs older-posts">
    <svg width="9" height="9" viewBox="0 0 10 10"><circle cx="5" cy="5" r="4.3" fill="none" stroke="#8a8a8a" stroke-width="1"/><path d="M4 3l3 2-3 2z" fill="#8a8a8a"/></svg>
    OLDER POSTS
  </div>

  <div class="abs excerpt excerpt-a">
    <p>Nulla neque urna, feugi at ac leo non, blandit aucto Etiam sit amet magna nec quam venenatis vehicula ut sed nislvcsNulla neque urna, feugi at ac leo non, blandit aucto Etiam sit amet magna nec quam venenatis vehicula ut sed nislvcsNulla neque urna, feugi at ac leo non, blandit aucto Etiam sit amet magna nec quam venenatis Nulla neque urna, feugi at ac leo non, blandit aucto Etiam sit amet magna nec quam venenatis vehicula ut sed nislvcsNulla neque urna, feugi at ac leo non, blandit aucto Etiam sit amet magna nec quam venenatis vehicula ut sed nislvcsNulla neque urna, feugi at ac leo non, blandit aucto Etiam sit amet magna nec quam venenatis</p>
  </div>
  <div class="abs media media-fire" role="img" aria-label="Illustration of a soldier firing into smoke"></div>

  <div class="abs media media-tower" role="img" aria-label="Illustration of a tall spire above a misty valley"></div>
  <div class="abs excerpt excerpt-b">
    <p>Nulla neque urna, feugi at ac leo non, blandit aucto Etiam sit amet magna nec quam venenatis vehicula ut sed nislvcsNulla neque urna, feugi at ac leo non, blandit aucto Etiam sit amet magna nec quam venenatis vehicula ut sed nislvcsNulla neque urna, feugi at ac leo non,</p>
    <p>Blandit aucto Etiam sit amet magna nec quam venenatis Nulla neque urna, feugi at ac leo non, blandit aucto Etiam sit amet magna nec quam venenatis vehicula ut sed nislvcsNulla neque urna, feugi at ac leo non, blandit aucto Etiam sit amet magna nec quam venenatis vehicula ut sed nislvcsNulla neque urna, feugi at ac leo non, blandit aucto Etiam sit amet magna nec quam venenatis</p>
  </div>

  <aside>
    <div class="abs" style="left:504px; top:465px;">
      <h3 class="widget-title">RECENT POSTS</h3>
      <ul class="widget-list" style="margin-top:14px;">
        <li>LACUS LEO FERMENT</li>
        <li>BULLA NEQUE ASTA</li>
        <li>QUAM VENENATIS UT SED</li>
        <li>FEUGI AT AC LEO</li>
        <li>LACUS LEO FERMENT</li>
      </ul>
    </div>
    <div class="abs" style="left:504px; top:589px;">
      <h3 class="widget-title">LINKS</h3>
      <ul class="widget-list" style="margin-top:14px;">
        <li>LACUS LEO FERMENT</li>
        <li>BULLA NEQUE ASTA</li>
        <li>QUAM VENENATIS UT SED</li>
        <li>FEUGI AT AC LEO</li>
        <li>LACUS LEO FERMENT</li>
      </ul>
    </div>
  </aside>
</main>

<section class="comments-band">
  <h2 class="comments-title">COMMENTS</h2>

  <article class="comment" style="left:99px;">
    <div class="avatar">
      <svg width="52" height="52" viewBox="0 0 52 52" aria-hidden="true"><circle cx="26" cy="21" r="7" fill="#8f8f8f"/><path d="M13 40c0-8 6-11 13-11s13 3 13 11z" fill="#8f8f8f"/></svg>
    </div>
    <div class="comment-body">
      <p class="comment-author">Nulla neque urna, feugi at</p>
      <p class="comment-sub">ac leo non, blandit aucto Etiam</p>
      <p class="comment-text">sit amet magna nec quam venenatis vehicula ut sed nislvcsNulla neque urna, feugi at ac leo non, blandit aucto Etiam sit amet magna nec quam venenatis vehicula ut sed nislvcsNulla neque urna, feugi at ac leo non</p>
      <a class="comment-reply" href="#">Reply</a>
    </div>
  </article>

  <article class="comment" style="left:364px;">
    <div class="avatar">
      <svg width="52" height="52" viewBox="0 0 52 52" aria-hidden="true"><circle cx="26" cy="21" r="7" fill="#8f8f8f"/><path d="M13 40c0-8 6-11 13-11s13 3 13 11z" fill="#8f8f8f"/></svg>
    </div>
    <div class="comment-body" style="left:69px;">
      <p class="comment-author">Nulla neque urna, feugi at</p>
      <p class="comment-sub">ac leo non, blandit aucto Etiam</p>
      <p class="comment-text">sit amet magna nec quam venenatis vehicula ut sed nislvcsNulla neque urna, feugi at ac leo non, blandit aucto Etiam sit amet magna nec quam venenatis vehicula ut sed nislvcsNulla neque urna, feugi at ac leo non</p>
      <a class="comment-reply" href="#">Reply</a>
    </div>
  </article>
</section>

<footer class="site-footer">
  <div class="footer-brand">
    <span class="line-1">Brindle Hollow</span>
    <span class="line-2">Studios</span>
  </div>
  <p class="footer-legal">© 2014 All Rights Reserved &nbsp;|&nbsp; Privacy Policy</p>
  <div class="footer-social" aria-label="Social links">
    <span></span><span></span><span></span><span></span>
  </div>
</footer>

</body>
</html>
```